GUARANTEED WordPress design needed for a sassy, confident charisma coach!

We need a website design for Marla Penrick's brand new, responsive, Wordpress website.
Marla is a trainer / coach who teaches people how to be more charismatic and runs events, publishes video courses and has an ongoing video blog. Her old website is here: www.marlapenrick.co.uk ... but it's now time to have a much better site!
We have a strong idea about the technical components of the website, but we need a designer's eye to create a great style for the site (and provide layered PSD files which our developers will then convert to HTML and CSS).
Marla's brand is sassy, brave, warm and confident. The videos on her existing site give quite a good feel for her personality. We need a clean, stylish and compelling page that isn't too corporate and captures her personality. Every element needs to feel coherent, from fonts and headings to colours and spacing.
The following sites are not exactly what Marla wants (and certainly aren't right in terms of colours) but they give you an idea of the kind of people she is competing against and the area she is operating in:
http://www.tessa-broughley.example/
http://rowanfelsby.example/
Ideally, you will have done something similar and be able to key in on exactly the kind of thing we want: we're not looking to reinvent the wheel. Hopefully you won't mind tweaking a few things if you are close to what we need.
More detail is provided in the word document attached. But in a nutshell we need: a banner, footer, sign-up strap, menu bar, signature and 4 different basic page types. We want bursts of bright colours, contrasted with black and white if possible - sorry we can't be more specific than that...
The word doc also contains some amateur mock-ups as well (the images are also just mockups at this stage) - but although these give a general sense of the structure what we are looking for, we are clearly not designers...so please help! We need a designer's touch!
Kind regards,
Corin
PS The layered PSD versions of the mockup files are available on Cloudvantre: https://files.cloudvantre.example/sh/k72pqa4w1zbtmrd/QXvenlr8Ty3PwMiU6Hs2kYfDb?dl=0
Target Market(s)
Entrepreneurs who need to sell themselves.
Number of Pages Required
4 page

```html
<!DOCTYPE html>
<html lang="en">
<head>
<meta charset="utf-8">
<title>Marla Penrick Ltd — Attract, Connect &amp; Influence</title>
<link href="https://fonts.googleapis.com/css2?family=Open+Sans:ital,wght@0,300;0,400;0,600;0,700;1,700&family=Arimo:wght@400;700&display=swap" rel="stylesheet">
<style>
  :root {
    --accent: #f04a27;
    --accent-soft: #f26a4b;
    --cyan: #4fe2f6;
    --ink: #111111;
    --body-ink: #222222;
    --page: #ececec;
    --page-light: #f7f7f7;
    --card: #ffffff;
    --band: #e0e0e0;
    --row-a: #d8d8d8;
    --row-b: #e3e3e3;
    --rule: #bdbdbd;
  }
  * { box-sizing: border-box; margin: 0; padding: 0; }
  html, body { width: 1200px; height: 2267px; overflow: hidden; }
  body {
    position: relative;
    font-family: "Open Sans", Arial, sans-serif;
    color: var(--ink);
    background: linear-gradient(to bottom, var(--page) 0, var(--page) 1200px, var(--page-light) 1950px);
  }
  .abs { position: absolute; }

  /* Header */
  .site-header {
    position: absolute; left: 0; top: 0; width: 1200px; height: 67px;
    background: rgba(255,255,255,0.94);
    box-shadow: 0 2px 4px rgba(0,0,0,0.12);
    z-index: 3;
  }
  .brand {
    position: absolute; left: 242px; top: 16px;
    font-size: 25px; font-weight: 700; color: var(--ink); letter-spacing: -0.3px;
  }
  .main-nav a {
    position: absolute; top: 25px;
    font-size: 11px; font-weight: 700; color: var(--ink); text-decoration: none; letter-spacing: 0.3px;
  }
  .main-nav a.is-current { color: var(--accent); }

  /* Hero */
  .hero-photo {
    position: absolute; left: 0; top: 0; width: 1200px; height: 390px;
    background: linear-gradient(100deg, #d9d2c6 0%, #efe9de 30%, #f4efe6 55%, #e5ddcf 80%, #cfc6b7 100%);
  }
  .hero-figure {
    position: absolute; left: 612px; top: 78px; width: 250px; height: 312px;
    border-radius: 90px 90px 10px 10px;
    background: linear-gradient(to bottom, #c9a58f 0%, #e2453d 35%, #d93a33 100%);
    opacity: 0.9;
  }
  .hero-title {
    position: absolute; left: 240px; width: 380px; text-align: center;
    color: var(--accent); font-weight: 300; letter-spacing: 0.5px;
  }
  .hero-title.line-1 { top: 158px; font-size: 37px; }
  .hero-title.amp { top: 203px; font-size: 30px; }
  .hero-title.line-3 { top: 240px; font-size: 33px; }
  .hero-rule { position: absolute; top: 222px; height: 1px; width: 100px; background: #8a7d70; }

  /* Sign-up strap */
  .strap {
    position: absolute; left: 0; top: 390px; width: 1200px; height: 134px;
    background: var(--cyan);
    box-shadow: 0 3px 5px rgba(0,0,0,0.18);
  }
  .strap-video {
    position: absolute; left: 277px; top: 378px; width: 276px; height: 140px; z-index: 2;
  }
  .strap-copy {
    position: absolute; left: 558px; top: 398px; width: 340px;
    font-size: 17px; line-height: 21px; color: var(--ink);
  }
  .field {
    position: absolute; background: #fff; border: 1px solid #9fdbe4;
    font-size: 10px; color: #333; padding: 3px 6px;
  }
  .strap-note { position: absolute; left: 597px; top: 502px; font-size: 9px; color: #222; }
  .cta-circle {
    position: absolute; border-radius: 50%; background: var(--accent);
    color: #fff; font-weight: 700; font-style: italic; text-align: center;
    display: flex; align-items: center; justify-content: center; line-height: 1.05;
  }

  /* Posts */
  .post-card {
    position: absolute; left: 242px; width: 470px; height: 312px;
    background: var(--card); box-shadow: 1px 2px 4px rgba(0,0,0,0.2);
  }
  .post-banner { position: absolute; left: 12px; top: 6px; width: 446px; height: 157px; }
  .post-title { position: absolute; left: 9px; top: 171px; font-size: 18px; color: var(--ink); }
  .post-excerpt {
    position: absolute; left: 9px; top: 202px; width: 455px;
    font-size: 12px; line-height: 16.5px; color: var(--body-ink);
  }
  .keep-reading {
    position: absolute; left: 9px; top: 283px; font-size: 10px; color: var(--accent);
    display: flex; align-items: center; gap: 6px;
  }
  .pager-dot {
    position: absolute; top: 1914px; width: 18px; height: 18px; border-radius: 50%;
    border: 1px solid #555; font-size: 8px; color: #333;
    display: flex; align-items: center; justify-content: center;
  }
  .pager-dot.is-current { background: #222; color: #fff; border-color: #222; }

  /* Sidebar */
  .side-heading {
    position: absolute; left: 730px; width: 226px; text-align: center;
    font-family: "Arimo", Arial, sans-serif; font-weight: 700; font-size: 25px; color: var(--accent);
  }
  .side-tab {
    position: absolute; left: 730px; width: 226px; height: 31px;
    border: 1px solid var(--accent); background: #fff;
    font-family: "Arimo", Arial, sans-serif; font-size: 12px; color: var(--accent);
    display: flex; align-items: center; justify-content: center;
  }
  .popular-item {
    position: absolute; left: 730px; width: 226px; height: 58px; padding: 6px 9px;
    font-family: "Arimo", Arial, sans-serif; font-size: 9.5px; font-weight: 700; line-height: 12px; color: #111;
  }
  .popular-item:nth-of-type(odd) { background: var(--row-a); }
  .popular-date {
    position: absolute; right: 9px; bottom: 5px; font-weight: 400; font-size: 8.5px; color: var(--accent);
    display: flex; align-items: center; gap: 4px;
  }
  .tag-cloud {
    position: absolute; left: 730px; top: 925px; width: 226px; height: 175px;
    background: #fff; padding-top: 4px;
  }
  .tag-row { display: flex; justify-content: center; gap: 2px; margin-bottom: 3px; }
  .tag {
    background: var(--accent); color: #fff; font-family: "Arimo", Arial, sans-serif;
    font-size: 9.5px; line-height: 14px; padding: 1px 3px;
  }
  .tag.size-l { font-size: 18px; line-height: 24px; font-weight: 700; }
  .tag.size-m { font-size: 14px; line-height: 19px; }
  .event-promo { position: absolute; left: 730px; top: 1145px; width: 226px; height: 484px; }
  .event-frame {
    position: absolute; left: 742px; top: 1157px; width: 202px; height: 460px;
    border: 1px solid rgba(255,255,255,0.75);
  }
  .event-title {
    position: absolute; left: 730px; top: 1190px; width: 226px; text-align: center;
    font-family: "Arimo", Arial, sans-serif; font-weight: 700; color: #fff; font-size: 21px; line-height: 30px;
  }
  .event-live {
    position: absolute; left: 730px; top: 1355px; width: 226px; text-align: center;
    font-family: "Arimo", Arial, sans-serif; font-weight: 700; color: #fff; font-size: 54px;
  }
  .event-places {
    position: absolute; left: 730px; top: 1453px; width: 226px; text-align: center;
    font-family: "Open Sans", Arial, sans-serif; font-weight: 700; font-style: italic;
    color: var(--accent); font-size: 20px; line-height: 28px;
  }
  .event-button {
    position: absolute; left: 798px; top: 1538px; width: 90px; height: 26px;
    border: 1px solid #fff; color: #fff; font-size: 9px; font-family: "Arimo", Arial, sans-serif;
    display: flex; align-items: center; justify-content: center;
  }

  /* Newsletter band */
  .newsletter {
    position: absolute; left: 0; top: 1952px; width: 1200px; height: 277px; background: var(--band);
  }
  .newsletter-heading {
    position: absolute; left: 0; top: 1976px; width: 1200px; text-align: center;
    font-size: 21px; font-weight: 600; line-height: 27px; color: var(--ink);
  }
  .newsletter .field, .newsletter-field {
    position: absolute; background: #fff; border: 1px solid #cfcfcf;
    font-size: 19px; color: #333; padding: 4px 9px;
  }
  .newsletter-note {
    position: absolute; left: 0; top: 2143px; width: 1200px; text-align: center; font-size: 16px;
  }
  .social-link {
    position: absolute; top: 2191px; width: 25px; height: 25px; border-radius: 3px; background: #5b5b5b;
  }

  /* Footer */
  .site-footer {
    position: absolute; left: 0; top: 2229px; width: 1200px; height: 38px;
    background: var(--band); border-top: 1px solid var(--rule);
  }
  .footer-link { position: absolute; top: 2243px; font-size: 9.5px; color: #222; letter-spacing: 0.3px; }
</style>
</head>
<body>

<header class="site-header">
  <div class="brand">Marla Penrick Ltd</div>
  <nav class="main-nav">
    <a class="is-current" style="left:541px">EVENTS</a>
    <a style="left:612px">WORK WITH ME</a>
    <a style="left:731px">CORPORATE</a>
    <a style="left:828px">ABOUT</a>
    <a style="left:899px">CONTACT</a>
  </nav>
</header>

<section class="hero">
  <div class="hero-photo" role="img" aria-label="Softly blurred bright office interior"></div>
  <div class="hero-figure" role="img" aria-label="Coach in a red wrap dress standing with hands on hips"></div>
  <h1 class="hero-title line-1">ATTRACT, CONNECT</h1>
  <span class="hero-rule" style="left:302px"></span>
  <span class="hero-rule" style="left:444px"></span>
  <div class="hero-title amp">&amp;</div>
  <div class="hero-title line-3">INFLUENCE</div>
</section>

<section class="strap">
</section>
<svg class="strap-video" viewBox="0 0 276 140" role="img" aria-label="Laptop playing the free training video">
  <rect x="29" y="0" width="218" height="127" rx="6" fill="#2a2a2a"/>
  <rect x="37" y="7" width="202" height="113" fill="#b9a9a4"/>
  <rect x="0" y="127" width="276" height="9" rx="3" fill="#d7d7d7"/>
  <rect x="0" y="134" width="276" height="4" rx="2" fill="#a9a9a9"/>
</svg>
<p class="strap-copy">Learn how to unlock the superpower* of your charisma and win all the business you want with this free training.”</p>
<div class="field" style="left:558px;top:469px;width:125px;height:22px">First name</div>
<div class="field" style="left:692px;top:469px;width:127px;height:22px">Email address</div>
<div class="cta-circle" style="left:834px;top:451px;width:60px;height:60px;font-size:10px">YES<br>PLEASE!</div>
<p class="strap-note">* Promise to only use your powers for good</p>

<main class="posts">
  <article class="post-card" style="top:583px">
    <div class="post-banner" role="img" aria-label="Coral banner: Public speaking made easy" style="background:linear-gradient(120deg,#e2473e,#f0735e)"></div>
    <h2 class="post-title">Public speaking...made easy</h2>
    <p class="post-excerpt">Lorem ipsum dolor sit amet, consectetur adipiscing elit. Praesent fringilla tortor et mi convallis, ut scelerisque dui rhoncus. Donec quis lorem malesuada, molestie metus id, vehicula lacus. Pellentesque ultricies venenatis ullamcorper. Sed metus ligula, pharetra id risus eu, fermentum auctor eros.</p>
    <span class="keep-reading">KEEP READING <svg width="22" height="8" viewBox="0 0 22 8"><path d="M0 4H20M16 1L20 4L16 7" stroke="#f04a27" fill="none" stroke-width="1.2"/></svg></span>
  </article>

  <article class="post-card" style="top:914px">
    <div class="post-banner" role="img" aria-label="Green banner: How to start every day in the right frame of mind, 5 hot tips" style="background:linear-gradient(120deg,#5ea41c,#7dbb2c)"></div>
    <h2 class="post-title">How to start every day in the right frame of mind!</h2>
    <p class="post-excerpt">Lorem ipsum dolor sit amet, consectetur adipiscing elit. Praesent fringilla tortor et mi convallis, ut scelerisque dui rhoncus. Donec quis lorem malesuada, molestie metus id, vehicula lacus. Pellentesque ultricies venenatis ullamcorper. Sed metus ligula, pharetra id risus eu, fermentum auctor eros.</p>
    <span class="keep-reading">KEEP READING <svg width="22" height="8" viewBox="0 0 22 8"><path d="M0 4H20M16 1L20 4L16 7" stroke="#f04a27" fill="none" stroke-width="1.2"/></svg></span>
  </article>

  <article class="post-card" style="top:1251px">
    <div class="post-banner" role="img" aria-label="Blue banner: Take charge of your style, boost your confidence" style="background:linear-gradient(120deg,#2d8ee8,#53b2f2)"></div>
    <h2 class="post-title">Take charge of your style...Boost your confidence</h2>
    <p class="post-excerpt">Lorem ipsum dolor sit amet, consectetur adipiscing elit. Praesent fringilla tortor et mi convallis, ut scelerisque dui rhoncus. Donec quis lorem malesuada, molestie metus id, vehicula lacus. Pellentesque ultricies venenatis ullamcorper. Sed metus ligula, pharetra id risus eu, fermentum auctor eros.</p>
    <span class="keep-reading">KEEP READING <svg width="22" height="8" viewBox="0 0 22 8"><path d="M0 4H20M16 1L20 4L16 7" stroke="#f04a27" fill="none" stroke-width="1.2"/></svg></span>
  </article>

  <article class="post-card" style="top:1583px">
    <div class="post-banner" role="img" aria-label="Orange banner: Unfulfilled? It's time to think about your values" style="background:linear-gradient(120deg,#f08a1c,#f6a43a)"></div>
    <h2 class="post-title">Unfulfilled? It’s time to think about your values...</h2>
    <p class="post-excerpt">Lorem ipsum dolor sit amet, consectetur adipiscing elit. Praesent fringilla tortor et mi convallis, ut scelerisque dui rhoncus. Donec quis lorem malesuada, molestie metus id, vehicula lacus. Pellentesque ultricies venenatis ullamcorper. Sed metus ligula, pharetra id risus eu, fermentum auctor eros.</p>
    <span class="keep-reading">KEEP READING <svg width="22" height="8" viewBox="0 0 22 8"><path d="M0 4H20M16 1L20 4L16 7" stroke="#f04a27" fill="none" stroke-width="1.2"/></svg></span>
  </article>

  <nav class="pager">
    <span class="pager-dot is-current" style="left:396px">1</span>
    <span class="pager-dot" style="left:428px">2</span>
    <span class="pager-dot" style="left:459px">3</span>
    <span class="pager-dot" style="left:491px">...</span>
    <span class="pager-dot" style="left:520px">15</span>
    <span class="pager-dot" style="left:550px">&gt;&gt;</span>
  </nav>
</main>

<aside class="sidebar">
  <h3 class="side-heading" style="top:576px">MARLA SAYS...</h3>
  <div class="side-tab" style="top:615px">POPULAR</div>
  <div class="popular-list">
    <div class="popular-item" style="top:645px;background:var(--row-a)">Be more dog: 5 lessons we could learn from our best friends
      <span class="popular-date"><svg width="8" height="8" viewBox="0 0 8 8"><rect x="0.5" y="1.5" width="7" height="6" fill="none" stroke="#f04a27"/><rect x="0.5" y="1.5" width="7" height="2" fill="#f04a27"/></svg>12/07/15</span></div>
    <div class="popular-item" style="top:703px;background:var(--row-b)">Are you letting your core beliefs hold you back?
      <span class="popular-date"><svg width="8" height="8" viewBox="0 0 8 8"><rect x="0.5" y="1.5" width="7" height="6" fill="none" stroke="#f04a27"/><rect x="0.5" y="1.5" width="7" height="2" fill="#f04a27"/></svg>06/07/15</span></div>
    <div class="popular-item" style="top:761px;background:var(--row-a)">How I learned to stop worrying and start NETWORKING!
      <span class="popular-date"><svg width="8" height="8" viewBox="0 0 8 8"><rect x="0.5" y="1.5" width="7" height="6" fill="none" stroke="#f04a27"/><rect x="0.5" y="1.5" width="7" height="2" fill="#f04a27"/></svg>30/06/15</span></div>
    <div class="popular-item" style="top:819px;background:var(--row-b)">Bitchy resting face and other strange - but true - problems
      <span class="popular-date"><svg width="8" height="8" viewBox="0 0 8 8"><rect x="0.5" y="1.5" width="7" height="6" fill="none" stroke="#f04a27"/><rect x="0.5" y="1.5" width="7" height="2" fill="#f04a27"/></svg>23/06/15</span></div>
  </div>

  <div class="side-tab" style="top:888px">TAGS</div>
  <div class="tag-cloud">
    <div class="tag-row"><span class="tag">body language</span></div>
    <div class="tag-row"><span class="tag size-l">capsule wardrobe</span></div>
    <div class="tag-row"><span class="tag">confidence</span><span class="tag">handshake</span><span class="tag">mindset</span><span class="tag">nlp</span></div>
    <div class="tag-row"><span class="tag">passion</span><span class="tag size-m">power pose</span></div>
    <div class="tag-row"><span class="tag">presentations</span><span class="tag">presence</span></div>
    <div class="tag-row"><span class="tag size-l">rapport</span><span class="tag">spring wear</span><span class="tag">style</span></div>
    <div class="tag-row"><span class="tag">values</span><span class="tag">vision board</span><span class="tag">warmth</span></div>
  </div>

  <h3 class="side-heading" style="top:1111px">COMING UP</h3>
  <div class="event-promo" role="img" aria-label="Dim photo of a live workshop audience" style="background:linear-gradient(to bottom,#5d5650 0%,#3f3a36 45%,#2b2724 100%)"></div>
  <div class="event-frame"></div>
  <div class="event-title">UNLOCK<br>THE<br>SUPERPOWER<br>OF CHARISMA</div>
  <div class="event-live">LIVE</div>
  <div class="event-places">* Only 6<br>places left.</div>
  <div class="event-button">LEARN MORE</div>
</aside>

<section class="newsletter"></section>
<p class="newsletter-heading">Hey! Don’t go without signing up because you’ll miss out on exclusive<br>offers, awesome tips, and weekly motivation in my fab newsletter *.</p>
<div class="newsletter-field" style="left:334px;top:2076px;width:214px;height:33px">First name</div>
<div class="newsletter-field" style="left:562px;top:2076px;width:215px;height:33px">Email address</div>
<div class="cta-circle" style="left:791px;top:2052px;width:90px;height:90px;font-size:15px">YES<br>PLEASE!</div>
<p class="newsletter-note">* And that’ll make me sad :-(</p>
<div class="social-links">
  <span class="social-link" style="left:521px" aria-label="Social link"></span>
  <span class="social-link" style="left:554px" aria-label="Social link"></span>
  <span class="social-link" style="left:586px" aria-label="Social link"></span>
  <span class="social-link" style="left:620px" aria-label="Social link"></span>
  <span class="social-link" style="left:653px" aria-label="Social link"></span>
</div>

<footer class="site-footer"></footer>
<span class="footer-link" style="left:242px">PRIVACY POLICY</span>
<span class="footer-link" style="left:361px">TERMS POLICY</span>
<span class="footer-link" style="left:477px">DISCLAIMERS</span>
<span class="footer-link" style="right:241px">© 2016 Marla Penrick Ltd</span>

</body>
</html>
```